Hello everyone,
I need someone to design a Business Card for my new company. It's called Norvakeep and we give procurement services of Chilean Salmon and Seafood in General. More specifically we are purchasing agents, quality inspectors and we help with general papework and logistics. Maybe in the future can open to some agriculture items such as Meat, Dairy Products and Fruits.
All this focused in international clients that cannot have the support they need when buying items from Chile.
A main concept is reliability.

Thank you in advance.

Esteban.

Target Market(s)

Salmon and Seafood Importers from all world.

Industry/Entity Type

Business

Contact Information for Business Card

The Name: Esteban Ruiz Pardo
My Mobile: +56 9 47316258
My Location: Puerto Melrin, Chile

Font styles to use
Serif
Sans Serif

Requirements
Must have
• The company name and a logo.
Nice to have
• Some full color on the back side.
Should not have
• No modern shapes. Just a rectangular business card. Remember that has to be accepted by a lot of different cultures, even senior Japanese clients.

```html
<!DOCTYPE html>
<html lang="en">
<head>
<meta charset="utf-8">
<title>Norvakeep Business Card</title>
<link rel="stylesheet" href="https://fonts.googleapis.com/css2?family=Crimson+Text:wght@400;600&display=swap">
<style>
  :root {
    --backdrop: #e6eaec;
    --card-dark: #1a1216;
    --card-light: #ffffff;
    --card-edge: #cfd8cf;
    --logo-ink: #46424a;
    --text-ink: #111111;
  }
  html, body {
    margin: 0;
    padding: 0;
    width: 1200px;
    height: 1110px;
    overflow: hidden;
    background: var(--backdrop);
  }
  .canvas {
    position: relative;
    width: 1200px;
    height: 1110px;
  }
  .card {
    position: absolute;
    left: 330px;
    width: 552px;
    height: 324px;
    box-sizing: border-box;
  }
  .card-front {
    top: 158px;
    height: 322px;
    background: var(--card-dark);
    display: flex;
    align-items: center;
    justify-content: center;
  }
  .brand-name {
    font-family: "Crimson Text", serif;
    font-weight: 400;
    font-size: 46px;
    color: var(--logo-ink);
    letter-spacing: 1px;
    margin-top: -8px;
  }
  .card-back {
    top: 613px;
    background: var(--card-light);
    border: 1px solid var(--card-edge);
  }
  .contact {
    position: absolute;
    right: 29px;
    bottom: 30px;
    text-align: right;
    font-family: "Crimson Text", serif;
    color: var(--text-ink);
  }
  .contact-name {
    font-weight: 600;
    font-size: 15px;
    margin: 0 0 15px;
    letter-spacing: 0.2px;
  }
  .contact-line {
    font-size: 14px;
    line-height: 17px;
    margin: 0;
  }
</style>
</head>
<body>
  <main class="canvas">
    <section class="card card-front">
      <span class="brand-name">Norvakeep</span>
    </section>
    <section class="card card-back">
      <div class="contact">
        <p class="contact-name">Esteban Ruiz Pardo</p>
        <p class="contact-line">+56 9 47316258</p>
        <p class="contact-line">Puerto Melrin, Chile</p>
      </div>
    </section>
  </main>
</body>
</html>
```